Real Estate "For Sale" Sign for construction company

We need a sign that we can use to hang on a post and place on the road when we sell a property. The sign will be simple and will need to mainly feature our logo (files attached), as well as the words "For Sale", and then our phone number "(555) 617 3489". The sign will hang on a post that'll look something like the attached picture.

Target Market(s)

Home buyers

Industry/Entity Type

Real Estate

Font styles to use
Serif
Sans Serif

Colors
0054AA
0677BA
7BADD7
CADEEF
E8F1F8
0094D4
00A9DD
6FCCEA
C7EBF8
E9F6FB

Requirements
Must have
• For Sale & our phone number

```html
<!DOCTYPE html>
<html lang="en">
<head>
<meta charset="utf-8">
<title>For Sale Sign – Ridgecrest Homes</title>
<link rel="stylesheet" href="https://fonts.googleapis.com/css2?family=Roboto:wght@400;900&display=swap">
<style>
  :root {
    --panel-dark: #353535;
    --panel-light: #ebebeb;
    --sign-white: #ffffff;
    --sale-red: #d0190f;
    --brand-navy: #062d7c;
    --ink-dark: #222222;
    --rule-dark: #333333;
  }
  * { margin: 0; padding: 0; box-sizing: border-box; }
  html, body { width: 1200px; height: 1200px; overflow: hidden; }
  body {
    position: relative;
    background: var(--panel-light);
    font-family: "Roboto", Arial, sans-serif;
  }
  .presentation-panel {
    position: absolute;
    top: 0;
    width: 600px; height: 1200px;
  }
  .presentation-panel--dark { left: 0; background: var(--panel-dark); }
  .presentation-panel--light { left: 600px; background: var(--panel-light); }

  .sign {
    position: absolute;
    width: 300px; height: 450px;
    background: var(--sign-white);
    text-align: center;
  }
  .sign--navy { left: 150px; top: 98px; }
  .sign--red { left: 150px; top: 652px; }
  .sign--featured {
    left: 150px; top: 375px;
    box-shadow: 0 18px 40px rgba(0, 0, 0, 0.18);
  }

  .sign__headline {
    position: absolute;
    left: 0; right: 0;
    font-family: "Roboto", Arial, sans-serif;
    font-weight: 900;
    color: var(--sale-red);
    line-height: 1;
  }
  .sign__headline--for { top: 47px; font-size: 72px; letter-spacing: 1px; }
  .sign__headline--sale { top: 110px; font-size: 96px; letter-spacing: 1px; }

  .sign__rule {
    position: absolute;
    left: 18px; right: 18px; top: 216px;
    height: 1px;
  }
  .sign--navy .sign__rule,
  .sign--featured .sign__rule { background: var(--sale-red); }
  .sign--red .sign__rule { background: var(--rule-dark); }

  .sign__prompt {
    position: absolute;
    left: 0; right: 0; top: 237px;
    font-size: 14px;
    line-height: 1;
    letter-spacing: -0.3px;
  }
  .sign__phone {
    position: absolute;
    left: 0; right: 0; top: 255px;
    font-family: "Roboto", Arial, sans-serif;
    font-weight: 900;
    font-size: 38px;
    line-height: 1;
    letter-spacing: -0.3px;
  }
  .sign--navy .sign__prompt, .sign--navy .sign__phone,
  .sign--featured .sign__prompt, .sign--featured .sign__phone { color: var(--brand-navy); }
  .sign--red .sign__prompt, .sign--red .sign__phone { color: var(--ink-dark); }

  .sign__brand-band {
    position: absolute;
    left: 15px; right: 15px; top: 322px;
    height: 112px;
    display: flex;
    align-items: center;
    justify-content: center;
    gap: 10px;
  }
  .sign--navy .sign__brand-band,
  .sign--featured .sign__brand-band { background: var(--brand-navy); }
  .sign--red .sign__brand-band { background: var(--sale-red); }

  .brand-mark {
    width: 14px; height: 14px;
    border-radius: 50%;
    background: var(--sign-white);
  }
  .brand-name {
    font-family: "Roboto", Arial, sans-serif;
    font-weight: 400;
    font-size: 22px;
    color: var(--sign-white);
    letter-spacing: 0.3px;
  }
</style>
</head>
<body>
  <div class="presentation-panel presentation-panel--dark">
    <section class="sign sign--navy">
      <div class="sign__headline sign__headline--for">FOR</div>
      <div class="sign__headline sign__headline--sale">SALE</div>
      <div class="sign__rule"></div>
      <p class="sign__prompt">CALL OR TEXT ME AT:</p>
      <p class="sign__phone">(555)617 3489</p>
      <div class="sign__brand-band">
        <span class="brand-mark"></span>
        <span class="brand-name">Ridgecrest Homes</span>
      </div>
    </section>

    <section class="sign sign--red">
      <div class="sign__headline sign__headline--for">FOR</div>
      <div class="sign__headline sign__headline--sale">SALE</div>
      <div class="sign__rule"></div>
      <p class="sign__prompt">CALL OR TEXT ME AT:</p>
      <p class="sign__phone">(555)617 3489</p>
      <div class="sign__brand-band">
        <span class="brand-mark"></span>
        <span class="brand-name">Ridgecrest Homes</span>
      </div>
    </section>
  </div>

  <div class="presentation-panel presentation-panel--light">
    <section class="sign sign--featured">
      <div class="sign__headline sign__headline--for">FOR</div>
      <div class="sign__headline sign__headline--sale">SALE</div>
      <div class="sign__rule"></div>
      <p class="sign__prompt">CALL OR TEXT ME AT:</p>
      <p class="sign__phone">(555)617 3489</p>
      <div class="sign__brand-band">
        <span class="brand-mark"></span>
        <span class="brand-name">Ridgecrest Homes</span>
      </div>
    </section>
  </div>
</body>
</html>
```